Public Speaking Book for aspiring, ambitious speakers

I'm looking for a 6x9 book cover (Parcelo standard) as well as ebook and audiobook formats.

I'm looking for orange font on a white background as these are my brand colours.

Feel free to use some yellow and gold too if you deem it appropriate.

Title: Climb and Glow
Subtitle: Find Your Voice. Tell Your Story. Share your Message.
Author: Lionel Barstow

I would like to have a picture of a female speaker on the front cover.

Alternatively, some kind of image that symbolises public speaking like a microphone, podium etc

Target Market(s)

Aspiring professional speakers

Colors
f78f20

Requirements
Must have
• Correct spelling!
Nice to have
• A logo or picture that fits the theme, but no pressure if you can't think of anything
Should not have
• No men in suits please. I don't want this to have a 1980s corporate look.

```html
<!DOCTYPE html>
<html lang="en">
<head>
<meta charset="UTF-8">
<title>Climb and Glow — Lionel Barstow</title>
<link rel="stylesheet" href="https://fonts.googleapis.com/css2?family=Montserrat:wght@400;500;600&display=swap">
<style>
  :root {
    --brand-orange: #f7901f;
    --ink: #111111;
    --paper: #ffffff;
    --crowd-crimson: #b01840;
    --crowd-orange: #ee6a10;
    --crowd-teal: #1aa090;
    --crowd-magenta: #c8185a;
    --crowd-purple: #4a1a5c;
  }
  html, body {
    margin: 0;
    padding: 0;
    overflow: hidden;
    background: var(--paper);
  }
  .cover {
    position: relative;
    width: 800px;
    height: 1200px;
    background: var(--paper);
    overflow: hidden;
    font-family: "Montserrat", sans-serif;
  }
  .title {
    position: absolute;
    top: 126px;
    left: 0;
    width: 100%;
    margin: 0;
    text-align: center;
    color: var(--brand-orange);
    font-weight: 500;
    font-size: 110px;
    line-height: 110px;
    letter-spacing: -2px;
    text-transform: uppercase;
    white-space: nowrap;
  }
  .title span { display: block; }
  .crowd-art {
    position: absolute;
    left: 240px;
    top: 494px;
    width: 321px;
    height: 222px;
    border-radius: 48px;
    background: linear-gradient(135deg,
      var(--crowd-purple) 0%,
      var(--crowd-crimson) 25%,
      var(--crowd-orange) 50%,
      var(--crowd-teal) 72%,
      var(--crowd-magenta) 100%);
    opacity: 0.9;
  }
  .subtitle {
    position: absolute;
    top: 738px;
    left: 0;
    width: 100%;
    margin: 0;
    text-align: center;
    color: var(--ink);
    font-weight: 500;
    font-size: 33px;
    line-height: 43px;
    letter-spacing: 3px;
  }
  .subtitle span { display: block; }
  .author {
    position: absolute;
    top: 1064px;
    left: 0;
    width: 100%;
    margin: 0;
    text-align: center;
    color: var(--brand-orange);
    font-weight: 500;
    font-size: 50px;
    letter-spacing: 1px;
  }
</style>
</head>
<body>
  <main class="cover">
    <h1 class="title"><span>Climb and</span><span>Glow</span></h1>

    <div class="crowd-art" role="img" aria-label="Illustration of speech bubbles filled with a colourful crowd of people in silhouette"></div>

    <p class="subtitle">
      <span>Find Your Voice.</span>
      <span>Tell Your Story.</span>
      <span>Share your Message.</span>
    </p>

    <p class="author">Lionel Barstow</p>
  </main>
</body>
</html>
```